Business Card Design Project

We need a new business card design that will allow us to incorporate three different logos. All three logos fall under our corporate name, Voltaro, Inc. Our current business card only has one logo on it. We have logo for our mobile printer division, a logo for our dot-matrix division, and a logo for our custom solutions division. I'd like all three logos to be on the new business card. I'd like the business card to have the same color scheme as our corporate web site: www.voltaro-example.com. We are a technology company that manufactures dot-matrix and mobile thermal printer. We also do custom OEM products as well.

Industry/Entity Type

Printer

Requirements
Must have
• all three logos on the business card

```html
<!DOCTYPE html>
<html lang="en">
<head>
<meta charset="utf-8">
<title>Voltaro Business Card</title>
<link href="https://fonts.googleapis.com/css2?family=Arimo:wght@400;700&display=swap" rel="stylesheet">
<style>
  :root {
    --backdrop: #2a2a2a;
    --card: #fbfbfb;
    --brand-blue: #1f7fc4;
    --band-blue: #2a86c6;
    --band-blue-dark: #1a6aa8;
    --ink: #1b1b1b;
    --rule: #6aa7d8;
  }
  * { margin: 0; padding: 0; box-sizing: border-box; }
  html, body {
    width: 1200px;
    height: 900px;
    overflow: hidden;
    background: var(--backdrop);
    font-family: "Arimo", Arial, sans-serif;
  }
  .card {
    position: absolute;
    left: 150px;
    top: 193px;
    width: 900px;
    height: 514px;
    background: var(--card);
    overflow: hidden;
  }
  .card__stripe {
    position: absolute;
    left: 0;
    right: 0;
    bottom: 84px;
    height: 9px;
    background: var(--ink);
  }
  .card__band {
    position: absolute;
    left: 0;
    right: 0;
    bottom: 0;
    height: 76px;
    background: linear-gradient(90deg, var(--band-blue-dark), var(--band-blue) 55%, var(--band-blue-dark));
  }
  .divisions {
    position: absolute;
    left: 70px;
    top: 78px;
    width: 350px;
    display: flex;
    flex-direction: column;
    gap: 48px;
  }
  .division {
    display: flex;
    align-items: center;
    gap: 12px;
    font-weight: 700;
    color: var(--ink);
    letter-spacing: 0.5px;
    white-space: nowrap;
  }
  .division__mark-square {
    flex: none;
    width: 30px;
    height: 30px;
    background: var(--brand-blue);
  }
  .division__mark-circle {
    flex: none;
    width: 36px;
    height: 36px;
    border-radius: 50%;
    background: var(--brand-blue);
  }
  .division--mobile { font-size: 24px; }
  .division--custom { font-size: 23px; color: var(--brand-blue); letter-spacing: 0; }
  .division--matrix { font-size: 38px; color: var(--brand-blue); }
  .card__divider {
    position: absolute;
    left: 445px;
    top: 55px;
    width: 2px;
    height: 255px;
    background: var(--rule);
  }
  .contact {
    position: absolute;
    left: 490px;
    top: 60px;
    color: var(--brand-blue);
  }
  .contact__name {
    font-size: 36px;
    font-weight: 400;
    line-height: 1.05;
  }
  .contact__title {
    font-size: 27px;
    line-height: 1.1;
    margin-bottom: 10px;
  }
  .contact__line {
    font-size: 21px;
    line-height: 1.45;
  }
  .contact__web { margin-top: 4px; }
</style>
</head>
<body>
  <div class="card">
    <div class="divisions">
      <div class="division division--mobile">
        <span class="division__mark-square"></span>
        <span>VOLTARO MOBILE</span>
      </div>
      <div class="division division--custom">
        <span class="division__mark-circle"></span>
        <span>Voltaro Custom Solutions</span>
      </div>
      <div class="division division--matrix">
        <span>VOLTARO</span>
      </div>
    </div>

    <div class="card__divider"></div>

    <div class="contact">
      <p class="contact__name">Daren Holt</p>
      <p class="contact__title">DESAINER</p>
      <p class="contact__line">Phone: (800) 555-0142</p>
      <p class="contact__line">Fax: (269) 555-0187</p>
      <p class="contact__line">e-mail: voltaro@mailbox-example.com</p>
      <p class="contact__line contact__web">www.voltaro-example.com</p>
    </div>

    <div class="card__stripe"></div>
    <div class="card__band"></div>
  </div>
</body>
</html>
```